Simple elegant feminine design - Going out on my own as a Mortgage Broker.
My thoughts are the following details on the Front, middle of the card possibly? Phone and email smaller font than my name?
Marnie Veltrin
Finance Specialist
p: 0438 215 962
e: marnie@veltrinlending.com.au
Bottom of the card
residential / commercial / equipment
I would like the Font in Rose Gold maybe white or black background? or Possibly a stone grey - are you able to do a few options? I'd like them embossed
Then I had an idea as a simple logo as per the attached if you get the idea in my scribble, my initials, capital M attached to a small v that leads/follows into a circle? Thicker Font In Rose Gold, middle of the card at the back.
Very open to ideas though and what colour you think would look better with the Rose Gold.
Thanks so much for your help, I am not very creative and savvy with this stuff :-)
Industry/Entity Type
Finance
Contact Information for Business Card
Marnie Veltrin
p: 0438 215 962
Look and feel

```html
<!DOCTYPE html>
<html lang="en">
<head>
<meta charset="utf-8">
<title>Marnie Veltrin – Business Card</title>
<link rel="stylesheet" href="https://fonts.googleapis.com/css2?family=Source+Sans+3:wght@400&display=swap">
<style>
  :root {
    --card-stone: #373a3d;
    --divider: #ffffff;
    --rose-gold: #e9aa9c;
    --rose-light: #f0c2b4;
    --gold: #d9b65e;
    --gold-deep: #9a7b2a;
    --ring: #e6a39a;
  }
  * { box-sizing: border-box; margin: 0; padding: 0; }
  html, body {
    width: 940px;
    height: 1200px;
    overflow: hidden;
    background: var(--divider);
    font-family: "Source Sans 3", "Myriad Pro", sans-serif;
  }
  .sheet {
    position: relative;
    width: 940px;
    height: 1200px;
  }
  .card {
    position: absolute;
    left: 0;
    width: 940px;
    background: var(--card-stone);
    overflow: hidden;
  }
  .card--front { top: 0; height: 593px; }
  .card--back { top: 601px; height: 599px; }

  .pattern {
    position: absolute;
    inset: 0;
    width: 100%;
    height: 100%;
  }

  .mark {
    position: absolute;
    border-radius: 50%;
    border: 2px solid var(--ring);
    display: flex;
    align-items: center;
    justify-content: center;
  }
  .card--front .mark {
    left: 325px;
    top: 148px;
    width: 298px;
    height: 298px;
  }
  .mark__name {
    color: var(--rose-gold);
    font-size: 30px;
    font-weight: 400;
  }
  .card--back .mark {
    left: 404px;
    top: 84px;
    width: 142px;
    height: 142px;
  }

  .identity {
    position: absolute;
    left: 556px;
    top: 120px;
  }
  .identity__name {
    color: var(--rose-light);
    font-size: 36px;
    font-weight: 400;
    line-height: 1;
    letter-spacing: 0.2px;
  }
  .identity__role {
    color: var(--rose-light);
    font-size: 17px;
    margin-left: 26px;
    margin-top: 4px;
    letter-spacing: 0.6px;
  }

  .contacts {
    position: absolute;
    left: 0;
    top: 0;
    list-style: none;
  }
  .contacts__item {
    position: absolute;
    display: flex;
    align-items: center;
    white-space: nowrap;
    color: var(--rose-light);
    font-size: 20px;
    letter-spacing: 1.4px;
  }
  .contacts__item--phone { left: 334px; top: 316px; }
  .contacts__item--email { left: 372px; top: 363px; }
  .contacts__item--services { left: 410px; top: 410px; }
  .contacts__bullet {
    width: 14px;
    height: 14px;
    border: 2px solid var(--rose-gold);
    transform: rotate(45deg);
    margin: 0 10px 0 4px;
    flex: none;
  }
</style>
</head>
<body>
<main class="sheet">

  <section class="card card--front" aria-label="Card front">
    <svg class="pattern" viewBox="0 0 940 593" role="img" aria-label="Rose gold and gold leaf pattern framing the card" preserveAspectRatio="none">
      <defs>
        <linearGradient id="frame-tone" x1="0" y1="0" x2="1" y2="1">
          <stop offset="0" stop-color="#e0b274"/>
          <stop offset="0.5" stop-color="#d7a07f"/>
          <stop offset="1" stop-color="#e2c070"/>
        </linearGradient>
      </defs>
      <path fill="url(#frame-tone)" fill-rule="evenodd"
            d="M0 0H940V593H0Z M153 125H788V466H153Z"/>
    </svg>
    <div class="mark">
      <span class="mark__name">Marnie Veltrin</span>
    </div>
  </section>

  <section class="card card--back" aria-label="Card back">
    <svg class="pattern" viewBox="0 0 940 599" role="img" aria-label="Faded gold leaf pattern in the top left corner" preserveAspectRatio="none">
      <defs>
        <linearGradient id="corner-tone" x1="0" y1="0" x2="1" y2="1">
          <stop offset="0" stop-color="#8d7433"/>
          <stop offset="0.6" stop-color="#6e6a5e"/>
          <stop offset="1" stop-color="#373a3d"/>
        </linearGradient>
      </defs>
      <rect x="0" y="0" width="370" height="336" fill="url(#corner-tone)"/>
    </svg>

    <div class="mark" aria-hidden="true"></div>

    <div class="identity">
      <h1 class="identity__name">Marnie Veltrin</h1>
      <p class="identity__role">Finance Specialiste</p>
    </div>

    <ul class="contacts">
      <li class="contacts__item contacts__item--phone"><span class="contacts__bullet"></span>0438 215 962</li>
      <li class="contacts__item contacts__item--email"><span class="contacts__bullet"></span>MARNIE@VELTRINLENDING.COM.AU</li>
      <li class="contacts__item contacts__item--services"><span class="contacts__bullet"></span>RESIDENTIAL / COMMERCIAL / EQUIPMENT</li>
    </ul>
  </section>

</main>
</body>
</html>
```